We need a tri-fold brochure for our business called: KindlePath. (KindlePath Therapy Services)
This is a therapy services business that offers Physiotherapy and Occupational Therapy to children aged 5 to 16 years of age. The focus is on Neuro-developmental therapy and the children have a range of conditions such as Cerebral-Palsy, brain injuries etc... We are looking for designs that focus on children, fun and the word nurture.
Target Market(s)
Primarily parents and people looking for therapy services.
Industry/Entity Type
Business
Font styles to use
Sans Serif

```html
<!DOCTYPE html>
<html lang="en">
<head>
<meta charset="utf-8">
<title>KindlePath Therapy Services – Tri-fold Brochure</title>
<link rel="stylesheet" href="https://fonts.googleapis.com/css2?family=Lato:ital,wght@0,400;0,700;1,400;1,700&family=Oswald:wght@600;700&display=swap">
<style>
  :root {
    --sky: #6ccbfb;
    --sky-deep: #1aa3f0;
    --magenta: #e600c8;
    --magenta-soft: #f58ae6;
    --paper: #ffffff;
    --paper-shade: #f2f2f2;
    --ink: #1a1a1a;
    --white: #ffffff;
  }
  * { margin: 0; padding: 0; box-sizing: border-box; }
  html, body { width: 1200px; height: 1024px; overflow: hidden; background: var(--paper); }
  .brochure {
    position: relative;
    width: 1200px;
    height: 1024px;
    font-family: "Lato", Arial, sans-serif;
    color: var(--ink);
    background: linear-gradient(90deg, var(--paper) 0%, var(--paper-shade) 33%, var(--paper) 34%, var(--paper-shade) 66.6%, var(--paper) 66.7%);
  }
  .artwork { position: absolute; inset: 0; }
  .panel-fold {
    position: absolute; top: 0; bottom: 0; width: 1px;
    background: rgba(0,0,0,0.06);
  }
  .about {
    position: absolute; left: 60px; top: 500px; width: 300px;
  }
  .about-title {
    font-style: italic; font-weight: 700; font-size: 17px;
    color: var(--magenta); text-align: center; margin-bottom: 10px;
  }
  .about-text {
    font-style: italic; font-size: 12px; line-height: 1.5; color: var(--ink);
  }
  .sky-note {
    position: absolute; left: 560px; top: 110px; width: 210px;
    color: var(--white); font-style: italic; font-weight: 700;
    font-size: 14px; line-height: 1.25; text-align: center;
  }
  .cloud-note {
    position: absolute; left: 500px; top: 455px; width: 200px;
    color: var(--white); font-style: italic; font-weight: 700;
    font-size: 16px; line-height: 1.25; text-align: center;
  }
  .contact {
    position: absolute; left: 420px; top: 690px; width: 360px;
    list-style: none; text-align: center;
  }
  .contact-item { margin-bottom: 14px; }
  .contact-icon { display: block; margin: 0 auto 4px; width: 20px; height: 20px; }
  .contact-phone { font-size: 28px; letter-spacing: 1px; }
  .contact-mail, .contact-address { font-size: 21px; }
  .brand-name {
    position: absolute; left: 800px; top: 42px; width: 400px;
    text-align: center; font-family: "Oswald", Arial, sans-serif;
    font-weight: 700; font-size: 46px; color: var(--magenta);
    text-transform: uppercase; letter-spacing: 1px;
  }
  .cover-title {
    position: absolute; left: 800px; top: 790px; width: 400px;
    text-align: center; color: var(--white);
  }
  .cover-name {
    font-family: "Oswald", Arial, sans-serif; font-weight: 700;
    font-size: 50px; text-transform: uppercase; line-height: 1.1;
  }
  .cover-sub {
    font-family: "Oswald", Arial, sans-serif; font-weight: 600;
    font-size: 19px; text-transform: uppercase; letter-spacing: 0.5px;
  }
  .cover-web { margin-top: 16px; font-size: 18px; }
</style>
</head>
<body>
<main class="brochure">
  <svg class="artwork" width="1200" height="1024" viewBox="0 0 1200 1024" xmlns="http://www.w3.org/2000/svg">
    <defs>
      <linearGradient id="playground-tones" x1="0" y1="0" x2="1" y2="1">
        <stop offset="0" stop-color="#4f7a3a"/>
        <stop offset="0.5" stop-color="#8fb36a"/>
        <stop offset="1" stop-color="#c9b49a"/>
      </linearGradient>
      <linearGradient id="jumping-tones" x1="0" y1="0" x2="1" y2="0">
        <stop offset="0" stop-color="#f3d6d6"/>
        <stop offset="0.35" stop-color="#b9dcf0"/>
        <stop offset="0.65" stop-color="#f6e3a8"/>
        <stop offset="1" stop-color="#d7e6f5"/>
      </linearGradient>
      <linearGradient id="cover-tones" x1="0" y1="0" x2="1" y2="1">
        <stop offset="0" stop-color="#ec4fd6"/>
        <stop offset="0.5" stop-color="#f06ddd"/>
        <stop offset="1" stop-color="#e22ccb"/>
      </linearGradient>
      <clipPath id="play-cloud">
        <circle cx="130" cy="150" r="60"/>
        <circle cx="200" cy="110" r="70"/>
        <circle cx="280" cy="120" r="65"/>
        <circle cx="320" cy="190" r="55"/>
        <circle cx="260" cy="240" r="62"/>
        <circle cx="170" cy="240" r="62"/>
        <circle cx="210" cy="180" r="80"/>
      </clipPath>
    </defs>

    <!-- sky band across inner panels -->
    <path class="sky-band-edge" fill="var(--sky-deep)"
      d="M0,0 H800 V108 C770,140 720,190 640,220 C600,236 590,262 600,292 C612,330 540,342 470,332 C420,324 400,312 380,342 C350,392 300,432 230,452 C150,472 60,482 0,492 Z"/>
    <path class="sky-band" fill="var(--sky)"
      d="M0,0 H800 V100 C770,130 720,180 640,210 C600,225 590,250 600,280 C610,318 540,330 470,320 C420,312 400,300 380,330 C350,380 300,420 230,440 C150,460 60,470 0,480 Z"/>

    <!-- bottom-left wave -->
    <path class="corner-wave-edge" fill="var(--sky-deep)" d="M0,892 C40,872 80,882 100,902 C140,942 200,990 266,1024 H0 Z"/>
    <path class="corner-wave" fill="var(--sky)" d="M0,900 C40,880 80,890 96,910 C136,950 196,994 250,1024 H0 Z"/>

    <!-- playground photo cloud -->
    <g class="photo-cloud-border" fill="var(--white)">
      <circle cx="130" cy="150" r="68"/>
      <circle cx="200" cy="110" r="78"/>
      <circle cx="280" cy="120" r="73"/>
      <circle cx="320" cy="190" r="63"/>
      <circle cx="260" cy="240" r="70"/>
      <circle cx="170" cy="240" r="70"/>
    </g>
    <rect class="photo-playground" x="60" y="30" width="330" height="280" fill="url(#playground-tones)"
      clip-path="url(#play-cloud)" role="img" aria-label="Photo of children playing tug of war in a park"/>

    <!-- magenta message cloud -->
    <g class="message-cloud-outline" fill="var(--magenta-soft)">
      <circle cx="530" cy="480" r="55"/>
      <circle cx="580" cy="440" r="58"/>
      <circle cx="650" cy="445" r="58"/>
      <circle cx="690" cy="500" r="52"/>
      <circle cx="650" cy="560" r="55"/>
      <circle cx="570" cy="565" r="55"/>
      <circle cx="600" cy="500" r="70"/>
    </g>
    <g class="message-cloud" fill="var(--magenta)">
      <circle cx="530" cy="480" r="47"/>
      <circle cx="580" cy="440" r="50"/>
      <circle cx="650" cy="445" r="50"/>
      <circle cx="690" cy="500" r="44"/>
      <circle cx="650" cy="560" r="47"/>
      <circle cx="570" cy="565" r="47"/>
      <circle cx="600" cy="500" r="62"/>
    </g>

    <!-- cover panel -->
    <rect class="photo-jumping" x="840" y="120" width="330" height="260" fill="url(#jumping-tones)"
      role="img" aria-label="Photo of a group of happy children jumping in the air"/>
    <rect class="photo-cover" x="800" y="410" width="400" height="614" fill="url(#cover-tones)"
      role="img" aria-label="Magenta-tinted photo of smiling children close together"/>
    <path class="cover-wave" fill="var(--magenta)"
      d="M800,385 C880,370 940,390 1000,420 C1070,455 1130,460 1200,440 V470 C1130,490 1070,485 1000,455 C940,428 880,412 800,425 Z"/>
    <path class="cover-wave-white" fill="var(--white)"
      d="M800,425 C880,412 940,428 1000,455 C1070,485 1130,490 1200,470 V485 C1130,505 1070,500 1000,470 C940,444 880,428 800,440 Z"/>
    <rect class="cover-base" x="800" y="780" width="400" height="244" fill="var(--magenta)" opacity="0.55"/>
  </svg>

  <div class="panel-fold" style="left:400px"></div>
  <div class="panel-fold" style="left:800px"></div>

  <section class="about">
    <h2 class="about-title">ABOUT US</h2>
    <p class="about-text">KindlePath supports children aged five to sixteen through gentle physiotherapy and occupational therapy. Our therapists focus on neuro-developmental care for conditions such as cerebral palsy and brain injury. Every session is built around play, trust and steady progress, so each child feels safe to try, move and grow. We work hand in hand with parents, sharing simple home routines and celebrating every small win along the way, nurturing confidence for life.</p>
  </section>

  <p class="sky-note">Lorem Ipsum is simply dummy text of the printing and typesetting industry</p>
  <p class="cloud-note">Lorem Ipsum is simply dummy text of the printing and typesetting industry</p>

  <ul class="contact">
    <li class="contact-item">
      <svg class="contact-icon" viewBox="0 0 20 20"><circle cx="10" cy="10" r="10" fill="var(--sky-deep)"/><path d="M7,5 L9,7 L8,9 C9,11 10,12 11,12 L13,11 L15,13 L13,15 C9,15 5,11 5,7 Z" fill="var(--white)"/></svg>
      <span class="contact-phone">XXX-XXX-XXX</span>
    </li>
    <li class="contact-item">
      <svg class="contact-icon" viewBox="0 0 20 20"><circle cx="10" cy="10" r="10" fill="var(--sky-deep)"/><rect x="5" y="6.5" width="10" height="7" fill="var(--white)"/><path d="M5,6.5 L10,10.5 L15,6.5" fill="none" stroke="var(--sky-deep)" stroke-width="1"/></svg>
      <span class="contact-mail">hello@kindlepath-care.com</span>
    </li>
    <li class="contact-item">
      <svg class="contact-icon" viewBox="0 0 20 20"><circle cx="10" cy="10" r="10" fill="var(--sky-deep)"/><path d="M10,4 C7.5,4 6,5.8 6,8 C6,11 10,16 10,16 C10,16 14,11 14,8 C14,5.8 12.5,4 10,4 Z" fill="var(--white)"/><circle cx="10" cy="8" r="1.6" fill="var(--sky-deep)"/></svg>
      <span class="contact-address">youaddress</span>
    </li>
  </ul>

  <div class="brand-name">KindlePath</div>

  <header class="cover-title">
    <h1 class="cover-name">KindlePath</h1>
    <p class="cover-sub">KindlePath Therapy Services</p>
    <p class="cover-web">www.kindlepath-care.com</p>
  </header>
</main>
</body>
</html>
```